Business Card Design

Velvet Pixel Promotions

An online marketing consulting & strategy business for the cosmetic niche

We specialise in Increasing Leads, Conversions & Content Marketing

I am looking for a very clean, BOLD business card that is simple & effective

Target Market(s)

cosmetic surgeons & cosmetic clinics

Industry/Entity Type

Marketing

Contact Information for Business Card

Darren Okoye
Online Marketing Strategist

Darren@VelvetPixelPromotions.example
0491 268 517

LinkedIn: in/darrenokoye

```html
<!DOCTYPE html>
<html lang="en">
<head>
<meta charset="utf-8">
<title>Velvet Pixel Promotions — Business Card</title>
<link href="https://fonts.googleapis.com/css2?family=Orbitron:wght@500&family=Roboto:wght@400;700&display=swap" rel="stylesheet">
<style>
  :root {
    --stage: #e7ebe6;
    --green-deep: #00873f;
    --green-mid: #1aa84a;
    --green-lime: #8cc63f;
    --teal: #1f8a78;
    --band: #0a3d1c;
    --band-edge: #06481f;
    --strip: #12983f;
    --strip-text: #b9e6a4;
    --ink-light: #f2f4f2;
    --ink-soft: #e8efe8;
  }
  * { box-sizing: border-box; margin: 0; padding: 0; }
  html, body { width: 1200px; height: 723px; overflow: hidden; }
  body {
    background: var(--stage);
    display: flex;
    align-items: center;
    justify-content: center;
    gap: 90px;
    font-family: "Roboto", Arial, sans-serif;
  }
  .card {
    position: relative;
    width: 370px;
    height: 605px;
    overflow: hidden;
    box-shadow: 0 12px 30px rgba(0,0,0,.22);
  }

  /* Front */
  .card--front {
    background: linear-gradient(160deg, var(--green-mid) 0%, var(--green-deep) 55%, var(--green-lime) 100%);
  }
  .front-field {
    position: absolute;
    left: 0; right: 0; top: 0;
    height: 400px;
    background: linear-gradient(150deg, #2bb150 0%, #12a04a 45%, #03904a 75%, #4fae3c 100%);
  }
  .brand {
    position: absolute;
    top: 58px; left: 0; right: 0;
    display: flex;
    flex-direction: column;
    align-items: center;
    gap: 22px;
  }
  .brand__dot {
    width: 74px; height: 74px;
    border-radius: 50%;
    background: var(--ink-light);
  }
  .brand__name {
    font-family: "Orbitron", "Arial Narrow", sans-serif;
    font-weight: 500;
    color: var(--ink-light);
    text-transform: uppercase;
    font-size: 33px;
    line-height: 1.02;
    letter-spacing: 2px;
    text-align: center;
  }
  .contact-band {
    position: absolute;
    left: 0; right: 0;
    top: 400px; height: 150px;
    background: linear-gradient(90deg, var(--band-edge), var(--band));
    padding: 20px 22px;
    display: flex;
    flex-direction: column;
    justify-content: space-between;
  }
  .contact {
    display: flex;
    align-items: center;
    gap: 10px;
    color: var(--ink-light);
    font-size: 15px;
  }
  .contact--email { font-size: 13.5px; }
  .contact__icon { width: 24px; height: 24px; flex: none; }
  .signature {
    position: absolute;
    left: 0; right: 0; bottom: 0;
    height: 55px;
    background: var(--strip);
    color: var(--strip-text);
    font-weight: 700;
    font-size: 15px;
    display: flex;
    align-items: center;
    padding-left: 22px;
  }

  /* Back */
  .card--back {
    background: linear-gradient(35deg, var(--teal) 0%, #2e9a5a 45%, var(--green-deep) 70%, var(--green-lime) 100%);
    display: flex;
    align-items: center;
    justify-content: center;
  }
  .card--back .brand {
    position: static;
    gap: 14px;
  }
  .card--back .brand__dot { width: 44px; height: 44px; background: var(--ink-soft); }
  .card--back .brand__name { font-size: 19px; letter-spacing: 1.5px; color: var(--ink-soft); }
</style>
</head>
<body>

<article class="card card--front">
  <div class="front-field" role="img" aria-label="Soft green faceted background pattern"></div>

  <div class="brand">
    <span class="brand__dot"></span>
    <h1 class="brand__name">Velvet<br>Pixel<br>Promotions</h1>
  </div>

  <div class="contact-band">
    <p class="contact">
      <svg class="contact__icon" viewBox="0 0 24 24" aria-hidden="true">
        <circle cx="12" cy="12" r="11" fill="#f2f4f2"/>
        <path d="M8.6 6.5l1.8-.3 1.1 2.9-1.2 1a7 7 0 0 0 3.6 3.6l1-1.2 2.9 1.1-.3 1.8c-.2.8-1 1.3-1.8 1.1A10 10 0 0 1 7.5 8.3c-.2-.8.3-1.6 1.1-1.8z" fill="#0a3d1c"/>
      </svg>
      0491 268 517
    </p>
    <p class="contact">
      <svg class="contact__icon" viewBox="0 0 24 24" aria-hidden="true">
        <circle cx="12" cy="12" r="11" fill="#f2f4f2"/>
      </svg>
      in/darrenokoye
    </p>
    <p class="contact contact--email">
      <svg class="contact__icon" viewBox="0 0 24 24" aria-hidden="true">
        <circle cx="12" cy="12" r="11" fill="#f2f4f2"/>
        <rect x="6" y="8" width="12" height="8.5" fill="none" stroke="#0a3d1c" stroke-width="1.4"/>
        <path d="M6 8l6 5 6-5" fill="none" stroke="#0a3d1c" stroke-width="1.4"/>
      </svg>
      Darren@VelvetPixelPromotions.example
    </p>
  </div>

  <p class="signature">Darren Okoye Online Marketing Strategist</p>
</article>

<article class="card card--back">
  <div class="brand">
    <span class="brand__dot"></span>
    <h2 class="brand__name">Velvet<br>Pixel<br>Promotions</h2>
  </div>
</article>

</body>
</html>
```